Email Design Creative Design Needed

Our website is called CampusLedger.org. One of our competitor(varsity scout.us.com) is using the following email creative.
http://qtr.brightvelmo.com/Affiliate/Assets/3532.html
http://qtr.brightvelmo.com/Affiliate/Assets/7921.html
http://qtr.brightvelmo.com/Affiliate/Assets/8061.html

We would like to use similar email creative without copying their exact creative. You can use the above as a guide but then come up with your own version of the creative.
The above are just concepts, please be creative and come up with your own version of it, without feeling that they have been copied. Feel free to move the components around. Also, feel free to change the colours and text.

Please find attached the CampusLedger.org logo.

Reason: We would like to receive more designs.

Industry/Entity Type

College

```html
<!DOCTYPE html>
<html lang="en">
<head>
<meta charset="utf-8">
<title>CampusLedger.org – Find Your Accredited Program</title>
<link href="https://fonts.googleapis.com/css2?family=Merriweather:wght@700;900&family=Source+Sans+3:wght@400;600;700&display=swap" rel="stylesheet">
<style>
:root{
  --navy:#14305a;
  --navy-deep:#0d2242;
  --amber:#f5a623;
  --amber-dark:#d9880c;
  --sky:#e8f0fa;
  --paper:#ffffff;
  --ink:#1c2533;
  --muted:#5b6676;
  --rule:#d6dfeb;
  --link:#1d6fd1;
  --photo-a:#c9a27a;
  --photo-b:#7e8fa8;
}
*{margin:0;padding:0;box-sizing:border-box}
html,body{width:900px;height:1200px;overflow:hidden;background:var(--paper)}
body{font-family:"Source Sans 3",Arial,sans-serif;color:var(--ink);position:relative}

.masthead{position:absolute;left:0;top:0;width:900px;height:96px;display:flex;align-items:center;padding:0 40px;gap:16px;border-bottom:4px solid var(--amber)}
.masthead__mark{width:34px;height:34px;background:var(--navy)}
.masthead__name{font-family:"Source Sans 3",Arial,sans-serif;font-size:40px;font-weight:700;color:var(--navy)}

.hero{position:absolute;left:0;top:100px;width:900px;height:440px;display:flex}
.hero__photo{width:360px;height:440px;background:linear-gradient(160deg,var(--photo-a) 0%,#a9876a 45%,var(--photo-b) 100%)}
.hero__panel{flex:1;background:var(--navy);color:#fff;padding:64px 48px 0 52px}
.hero__kicker{font-size:18px;font-weight:700;letter-spacing:3px;text-transform:uppercase;color:var(--amber)}
.hero__title{font-family:"Merriweather",Georgia,serif;font-weight:900;font-size:50px;line-height:60px;margin-top:16px}
.hero__sub{font-size:22px;line-height:31px;margin-top:18px;color:#d5e0ef;max-width:430px}
.hero__cta{display:inline-flex;align-items:center;gap:14px;margin-top:34px;height:60px;padding:0 30px;border-radius:8px;
  background:var(--amber);color:var(--navy-deep);font-size:22px;font-weight:700;text-decoration:none}

.section-title{position:absolute;left:40px;top:566px;font-family:"Merriweather",Georgia,serif;font-weight:700;font-size:26px;color:var(--navy)}

.careers{position:absolute;left:40px;top:614px;width:820px;border-collapse:collapse}
.careers th{height:44px;text-align:left;font-size:15px;font-weight:700;letter-spacing:1.5px;text-transform:uppercase;color:var(--muted);border-bottom:2px solid var(--navy)}
.careers td{height:60px;font-size:18px;border-bottom:1px solid var(--rule);vertical-align:middle}
.careers tbody tr:nth-child(even) td{background:var(--sky)}
.careers .col-career{width:440px;padding-left:16px;font-weight:600}
.careers .col-pay{width:190px;font-weight:700;color:var(--navy)}
.careers .col-link{text-align:right;padding-right:16px}
.careers th.col-career{padding-left:16px}
.careers th.col-link{text-align:right}
.careers a{color:var(--link);font-weight:700;text-decoration:none}

.fineprint{position:absolute;left:40px;top:1000px;width:820px;padding-top:20px;border-top:1px solid var(--rule);font-size:14px;line-height:21px;color:var(--muted)}
.fineprint p + p{margin-top:10px}
.fineprint a{color:var(--muted)}
</style>
</head>
<body>

<header class="masthead">
  <div class="masthead__mark"></div>
  <div class="masthead__name">CampusLedger.org</div>
</header>

<section class="hero">
  <div class="hero__photo" role="img" aria-label="Photo of a smiling college student holding a pen on campus"></div>
  <div class="hero__panel">
    <div class="hero__kicker">Your next chapter</div>
    <h1 class="hero__title">Earn a Degree That Moves You Forward</h1>
    <p class="hero__sub">Compare programs from accredited colleges and universities in one place.</p>
    <a class="hero__cta" href="#">Explore Programs
      <svg width="22" height="18" viewBox="0 0 22 18" aria-hidden="true"><path d="M2 9h16M11 2l7 7-7 7" fill="none" stroke="#0d2242" stroke-width="3" stroke-linecap="round" stroke-linejoin="round"/></svg>
    </a>
  </div>
</section>

<h2 class="section-title">Careers in Education</h2>

<table class="careers">
  <thead>
    <tr><th class="col-career">Career Path</th><th class="col-pay">Median Pay*</th><th class="col-link">Programs</th></tr>
  </thead>
  <tbody>
    <tr><td class="col-career">Education Administrator</td><td class="col-pay">$90,200 / yr</td><td class="col-link"><a href="#">Browse programs →</a></td></tr>
    <tr><td class="col-career">Elementary &amp; Secondary Teacher</td><td class="col-pay">$90,200 / yr</td><td class="col-link"><a href="#">Browse programs →</a></td></tr>
    <tr><td class="col-career">School &amp; Career Counselor</td><td class="col-pay">$56,540 / yr</td><td class="col-link"><a href="#">Browse programs →</a></td></tr>
    <tr><td class="col-career">Childcare Center Director</td><td class="col-pay">$51,290 / yr</td><td class="col-link"><a href="#">Browse programs →</a></td></tr>
    <tr><td class="col-career">Preschool Teacher</td><td class="col-pay">$30,150 / yr</td><td class="col-link"><a href="#">Browse programs →</a></td></tr>
  </tbody>
</table>

<footer class="fineprint">
  <p>*Median pay figures are based on data from the U.S. Bureau of Labor Statistics. Financial aid is available to those who qualify; speak with a representative of a partner school to check your eligibility.</p>
  <p>Results differ by institution and curriculum. Employment after graduation is not guaranteed.</p>
  <p>Prefer fewer emails? <a href="#">Unsubscribe here</a> or write to Brightvelmo Marketing Inc, PO Box 512204 #27145, Springfield, IL 62704-2204.</p>
</footer>

</body>
</html>
```